Travenic Professional Services Website

Small website for company presence and information. Company is an IT/Telecom services company. We provide presales and installation services. Included are various company logos including color levels. Site doesn't have to use these exact colors in the logos, but should be complimentary if using different colors. It should have a professional business appearance.
Updates

My apologies for not being more responsive on the designs that have been submitted. I will be narrowing down the submissions and providing additional feedback next week. Thank you for your patience.

Project Deadline Extended
Reason: Sorry again for delays on picking designs. Work has me very busy and I've just not had the time to devote to this project. I am extending the design deadline for a few more days to give me time to make my final decisions. Thank you all for your patience. Stay tuned....

Target Market(s)

Telecom sales companies that sell Brintel telecom products.

Industry/Entity Type

Professional Service

Coding

Coded - Design and coding required

Number of Pages Required

5+ page

Font styles to use
Sans Serif

Colors
3276b5
0355a3
85abd2
85cae6
33a6d7
0692cd
ffffff

Requirements
Must have
• Professional design reflective of IT/Telecom business. A good reference website would be: http://www.quollanetworks.example/. Looking for something similar in function and presence.
Nice to have
• Rolling photos highlighting our services. Traditional navigation across the top of all pages.
Should not have
• No motion video, flashy presentation or overly confused interface.

```html
<!DOCTYPE html>
<html lang="en">
<head>
<meta charset="utf-8">
<title>Travenic Professional Services</title>
<link href="https://fonts.googleapis.com/css2?family=Lato:wght@400;700;900&display=swap" rel="stylesheet">
<style>
  :root{
    --navy:#0355a3;
    --blue:#3276b5;
    --sky:#0692cd;
    --cyan:#33a6d7;
    --light:#85cae6;
    --pale:#85abd2;
    --white:#ffffff;
    --text:#7a7f86;
    --dark:#333a42;
    --band:#f7f7f7;
  }
  *{box-sizing:border-box;margin:0;padding:0}
  html,body{width:1200px;height:2853px;overflow:hidden}
  body{position:relative;font-family:"Lato",Arial,sans-serif;color:var(--text);background:var(--white)}
  .abs{position:absolute}

  /* Hero */
  .hero{position:absolute;left:0;top:0;width:1200px;height:590px;
    background:linear-gradient(180deg,#1877c9 0%,#2a8fdc 55%,#45a6e6 100%)}
  .hero-tower{position:absolute;left:752px;top:55px;width:105px;height:535px;
    background:linear-gradient(180deg,rgba(230,80,80,.55),rgba(240,240,240,.55))}
  .hero-cloud{position:absolute;left:1030px;top:400px;width:170px;height:190px;border-radius:90px 0 0 0;
    background:linear-gradient(160deg,rgba(255,255,255,.85),rgba(235,242,250,.95))}
  .brand{position:absolute;display:flex;align-items:center;gap:10px;color:var(--white);font-weight:900}
  .brand-mark{width:24px;height:24px;background:currentColor}
  .brand-name{font-size:22px;letter-spacing:1px;line-height:1}
  .brand-sub{display:block;font-size:7px;letter-spacing:1px;margin-top:3px}
  .menu-btn{position:absolute;left:922px;top:72px;width:38px;height:36px;background:var(--white);border-radius:4px;
    display:flex;align-items:center;justify-content:center}
  .menu-label{position:absolute;left:920px;top:113px;width:42px;text-align:center;color:var(--white);font-size:9px;font-weight:900}
  .hero-title{position:absolute;left:247px;top:252px;width:360px;color:var(--white);font-size:35px;font-weight:700;line-height:42px}
  .hero-copy{position:absolute;left:247px;top:352px;width:310px;color:var(--white);font-size:12px;line-height:19px}
  .btn-hero{position:absolute;left:247px;top:436px;width:132px;height:36px;background:var(--white);border-radius:4px;
    color:var(--dark);font-size:11px;font-weight:900;display:flex;align-items:center;justify-content:center;letter-spacing:.3px}
  .slider-dots{position:absolute;left:34px;top:380px}
  .slider-dots span{display:block;width:8px;height:8px;border-radius:50%;background:var(--white);margin-bottom:19px}
  .slider-dots span:first-child{background:#0b3f74}

  /* Headings & text */
  .h2{color:var(--navy);font-size:30px;font-weight:900}
  .body{font-size:11.5px;line-height:18px}
  .photo{position:absolute}

  /* Services */
  .band{position:absolute;left:0;width:1200px;background:var(--band)}
  .svc-list{list-style:none;font-size:11.5px}
  .svc-list li{height:21.5px;position:relative;padding-left:17px}
  .svc-list li::before{content:"›";position:absolute;left:0;top:-2px;font-size:14px}
  .play{position:absolute;left:753px;top:1182px;width:40px;height:40px;border-radius:50%;background:var(--white);
    display:flex;align-items:center;justify-content:center}

  /* What we do */
  .feature-title{position:absolute;color:var(--dark);font-size:15px;font-weight:900}
  .feature-icon{position:absolute;width:48px;height:48px}
  .btn-sm{position:absolute;width:64px;height:22px;background:var(--navy);border-radius:3px;color:var(--white);
    font-size:9px;font-weight:900;display:flex;align-items:center;justify-content:center}

  /* News */
  .news-date{position:absolute;color:var(--navy);font-size:9.5px;font-weight:900}
  .news-text{position:absolute;font-size:9.5px;line-height:15px;color:var(--dark);width:226px}

  /* Footer */
  .foot-head{position:absolute;color:var(--cyan);font-size:11px;font-weight:900;letter-spacing:.3px}
  .foot-links{position:absolute;list-style:none;font-size:11.5px;color:var(--dark);line-height:19px}
  .connect{position:absolute;left:824px;top:2809px;display:flex;align-items:center;gap:9px;font-size:8px;color:var(--dark)}
  .connect i{display:block;width:8px;height:8px;border-radius:50%;background:var(--cyan)}
  .copy{position:absolute;left:1126px;top:2809px;font-size:8px;color:var(--dark)}
</style>
</head>
<body>

<!-- Hero -->
<section class="hero" role="img" aria-label="Photo of a red and white telecom tower against a blue sky with clouds">
  <div class="hero-tower"></div>
  <div class="hero-cloud"></div>
</section>
<div class="brand" style="left:247px;top:74px">
  <span class="brand-mark"></span>
  <span class="brand-name">TRAVENIC<span class="brand-sub">PROFESSIONAL SERVICES</span></span>
</div>
<div class="menu-btn">
  <svg width="14" height="12" viewBox="0 0 14 12"><rect y="0" width="14" height="2.4" fill="#0355a3"/><rect y="4.8" width="14" height="2.4" fill="#0355a3"/><rect y="9.6" width="14" height="2.4" fill="#0355a3"/></svg>
</div>
<div class="menu-label">MENU</div>
<div class="slider-dots"><span></span><span></span><span></span><span></span></div>
<h1 class="hero-title">An IT/Telecom Services Company</h1>
<p class="hero-copy">Sed ut perspiciatis unde omnis iste natus error sit voluptatem accusantium doloremque laudantium, totam rem aperiam, eaque</p>
<a class="btn-hero">LEARN MORE</a>

<!-- Welcome -->
<div class="photo" role="img" aria-label="Photo of telecom antenna towers silhouetted at sunset" style="left:240px;top:683px;width:285px;height:264px;background:linear-gradient(180deg,#6f7f93 0%,#c59a6a 55%,#f0a23a 100%)"></div>
<h2 class="h2 abs" style="left:550px;top:702px">Welcome To Travenic</h2>
<p class="body abs" style="left:550px;top:773px;width:410px">Sed ut perspiciatis unde omnis iste natus error sit voluptatem accusantium doloremque laudantium, totam rem aperiam, eaque ipsa quae ab illo inventore veritatis et quasi architecto beatae vitae dicta sunt explicabo. Nemo enim ipsam voluptatem quia voluptas sit aspernatur aut odit aut fugit, sed quia consequuntur magni dolores eos qui ratione voluptatem sequi nesciunt.</p>
<p class="body abs" style="left:550px;top:883px;width:410px">Neque porro quisquam est, qui dolorem ipsum quia dolor sit amet, consectetur, adipisci velit, sed quia non numquam eius</p>

<!-- Our Services -->
<div class="band" style="top:1027px;height:356px"></div>
<h2 class="h2 abs" style="left:240px;top:1084px">Our Services</h2>
<p class="body abs" style="left:240px;top:1140px;width:390px">Raise the bar of your customer service for your end-customers with Norvane's tailored solutions and services for global telecom service providers/carriers.</p>
<ul class="svc-list abs" style="left:240px;top:1220px">
  <li>Robust off-the-shelf software systems</li>
  <li>Custom development services</li>
  <li>Business process optimization</li>
  <li>System integration for business support</li>
  <li>Operations support systems</li>
</ul>
<div class="photo" role="img" aria-label="Video still of a hand holding a glowing wireless signal" style="left:593px;top:1092px;width:364px;height:224px;border:3px solid #fff;box-shadow:0 0 0 1px #e2e2e2;background:radial-gradient(circle at 40% 65%,#f2a23a 0%,#4a3a3a 22%,#15171c 60%,#0d0e12 100%)"></div>
<div class="play"><svg width="14" height="16" viewBox="0 0 14 16"><path d="M2 1 L13 8 L2 15 Z" fill="#15171c"/></svg></div>

<!-- What We Do -->
<h2 class="h2 abs" style="left:0;top:1440px;width:1200px;text-align:center">What We Do ?</h2>
<p class="body abs" style="left:244px;top:1505px;width:713px;text-align:center">Sed ut perspiciatis unde omnis iste natus error sit voluptatem accusantium doloremque laudantium, totam rem aperiam, eaque ipsa quae ab illo inventore veritatis et quasi architecto beatae vitae dicta sunt explicabo. Nemo enim ipsam voluptatem quia voluptas sit aspernatur aut odit aut fugit, sed quia consequuntur magni dolores eos qui ratione voluptatem sequi nesciunt.</p>

<svg class="feature-icon" style="left:238px;top:1620px" viewBox="0 0 48 48"><circle cx="17" cy="13" r="9" fill="#3276b5"/><path d="M2 44 C2 30 10 25 17 25 C24 25 30 29 31 38 L31 44 Z" fill="#3276b5"/><path d="M36 18 C30 18 27 22 27 26 C27 32 36 42 36 42 C36 42 45 32 45 26 C45 22 42 18 36 18 Z" fill="#33a6d7"/><circle cx="36" cy="26" r="3.5" fill="#fff"/></svg>
<div class="feature-title" style="left:304px;top:1638px">Track Location</div>
<p class="body abs" style="left:240px;top:1696px;width:350px">Sed ut perspiciatis unde omnis iste natus error sit voluptatem accusantium doloremque laudantium, totam rem aperiam, eaque ipsa quae ab illo inventore veritatis et quasi</p>
<a class="btn-sm" style="left:240px;top:1778px">Read More</a>

<svg class="feature-icon" style="left:609px;top:1620px" viewBox="0 0 48 48"><circle cx="20" cy="14" r="9" fill="#3276b5"/><path d="M9 15 C9 6 31 6 31 15" fill="none" stroke="#0355a3" stroke-width="3"/><path d="M4 45 C4 32 11 27 20 27 C29 27 34 31 35 36 L35 45 Z" fill="#3276b5"/><circle cx="38" cy="38" r="7" fill="#33a6d7"/><path d="M35 38 L37.5 40.5 L41.5 35.5" stroke="#fff" stroke-width="2" fill="none"/></svg>
<div class="feature-title" style="left:671px;top:1638px">Maintenance</div>
<p class="body abs" style="left:609px;top:1696px;width:350px">Sed ut perspiciatis unde omnis iste natus error sit voluptatem accusantium doloremque laudantium, totam rem aperiam, eaque ipsa quae ab illo inventore veritatis et quasi</p>
<a class="btn-sm" style="left:609px;top:1778px">Read More</a>

<svg class="feature-icon" style="left:232px;top:1852px" viewBox="0 0 48 48"><path d="M40 20 A17 17 0 1 1 30 9" fill="none" stroke="#3276b5" stroke-width="4"/><path d="M15 23 L22 30 L40 8" fill="none" stroke="#33a6d7" stroke-width="5"/></svg>
<div class="feature-title" style="left:304px;top:1868px">Schedule Time</div>
<p class="body abs" style="left:240px;top:1926px;width:350px">Sed ut perspiciatis unde omnis iste natus error sit voluptatem accusantium doloremque laudantium, totam rem aperiam, eaque ipsa quae ab illo inventore veritatis et quasi</p>
<a class="btn-sm" style="left:240px;top:2008px">Read More</a>

<svg class="feature-icon" style="left:609px;top:1852px" viewBox="0 0 48 48"><rect x="6" y="4" width="36" height="11" rx="2" fill="#3276b5"/><rect x="6" y="18" width="36" height="11" rx="2" fill="#33a6d7"/><rect x="6" y="32" width="36" height="11" rx="2" fill="#3276b5"/><circle cx="12" cy="9.5" r="2" fill="#fff"/><circle cx="12" cy="23.5" r="2" fill="#fff"/><circle cx="12" cy="37.5" r="2" fill="#fff"/><rect x="20" y="8" width="16" height="3" fill="#fff"/><rect x="20" y="22" width="16" height="3" fill="#fff"/><rect x="20" y="36" width="16" height="3" fill="#fff"/></svg>
<div class="feature-title" style="left:671px;top:1868px">Server Locator</div>
<p class="body abs" style="left:609px;top:1926px;width:350px">Sed ut perspiciatis unde omnis iste natus error sit voluptatem accusantium doloremque laudantium, totam rem aperiam, eaque ipsa quae ab illo inventore veritatis et quasi</p>
<a class="btn-sm" style="left:609px;top:2008px">Read More</a>

<!-- News -->
<div class="band" style="top:2123px;height:432px"></div>
<h2 class="h2 abs" style="left:0;top:2170px;width:1200px;text-align:center">News</h2>

<div class="photo" role="img" aria-label="Photo of a businessman using a phone in front of a city at night" style="left:240px;top:2240px;width:226px;height:138px;background:linear-gradient(135deg,#2b3a5c 0%,#6a5a8c 50%,#b48ac0 100%)"></div>
<div class="news-date" style="left:240px;top:2393px">January 19th | 2016</div>
<p class="news-text" style="left:240px;top:2412px">Sed ut perspiciatis unde omnis iste natus error sit voluptatem accusantium</p>
<a class="btn-sm" style="left:240px;top:2454px">Read More</a>

<div class="photo" role="img" aria-label="Photo of hands using an office desk telephone" style="left:487px;top:2240px;width:226px;height:138px;background:linear-gradient(135deg,#e4e6ea 0%,#b9bec6 55%,#4a4e55 100%)"></div>
<div class="news-date" style="left:487px;top:2393px">January 19th | 2016</div>
<p class="news-text" style="left:487px;top:2412px">Sed ut perspiciatis unde omnis iste natus error sit voluptatem accusantium</p>
<a class="btn-sm" style="left:487px;top:2454px">Read More</a>

<div class="photo" role="img" aria-label="Photo of a telecom tower under a purple evening sky" style="left:732px;top:2240px;width:227px;height:138px;background:linear-gradient(180deg,#7e7fb8 0%,#b59ac8 50%,#e8c8d8 100%)"></div>
<div class="news-date" style="left:732px;top:2393px">January 19th | 2016</div>
<p class="news-text" style="left:732px;top:2412px">Sed ut perspiciatis unde omnis iste natus error sit voluptatem accusantium</p>
<a class="btn-sm" style="left:732px;top:2454px">Read More</a>

<!-- Footer -->
<div class="foot-head" style="left:240px;top:2612px">QUICK LINKS</div>
<ul class="foot-links" style="left:240px;top:2645px"><li>Home</li><li>Products</li><li>Services</li><li>Faq's</li><li>Contact Us</li></ul>
<div class="foot-head" style="left:436px;top:2612px">ABOUT US</div>
<ul class="foot-links" style="left:436px;top:2645px"><li>Careers</li><li>Leadership</li><li>Locations</li><li>Resources</li><li>News</li></ul>
<div class="foot-head" style="left:590px;top:2612px">OTHER LINKS</div>
<ul class="foot-links" style="left:590px;top:2645px"><li>Sitemap</li><li>Trademarks</li><li>Terms</li><li>Privacy Policy</li></ul>
<div class="foot-head" style="left:763px;top:2612px">SERVICES</div>
<ul class="foot-links" style="left:763px;top:2645px"><li>Core IT &amp; Telecom Services</li><li>Contact Centre Solutions</li><li>Telecom Expense Management</li><li>Data, Voice and Video networking</li></ul>

<div class="brand" style="left:240px;top:2800px;color:var(--navy)">
  <span class="brand-mark"></span>
  <span class="brand-name">TRAVENIC<span class="brand-sub">PROFESSIONAL SERVICES</span></span>
</div>
<div class="connect">CONNECT WITH US <i></i><i></i><i></i><i></i></div>
<div class="copy">CS</div>

</body>
</html>
```